Design a building access mobile app for Wopel by Quillstone Access Controls

Hello, We're looking for an awesome designer to create an app design for our app Wopel, by Quillstone Access Controls. the mobile app allows employees open their office doors with their mobile phone. this means they don't have to use those plastic card badges or keys. We like clean modern design, dark and light themes. We don't have a logo yet.

Target Market(s)

Commercial and employees

Industry/Entity Type

Building

Font styles to use
Sans Serif
Other font styles liked:
• Oswald extra light

Requirements
Must have
• nice clean design

```html
<!DOCTYPE html>
<html lang="en">
<head>
<meta charset="utf-8">
<title>Wopel — Building Access App Screens</title>
<link rel="stylesheet" href="https://fonts.googleapis.com/css2?family=Montserrat:wght@300;400;500;600;700&display=swap">
<style>
  :root {
    --canvas: #0d141b;
    --panel-dark: #161616;
    --panel-black: #050505;
    --header: #111111;
    --field: #2a2a2a;
    --accent: #00b2ff;
    --white: #ffffff;
    --light: #f2f2f2;
    --muted: #8a8a8a;
    --ink: #1a1a1a;
  }
  * { box-sizing: border-box; margin: 0; padding: 0; }
  html, body { width: 1200px; height: 1200px; overflow: hidden; }
  body {
    background: var(--canvas);
    font-family: "Montserrat", sans-serif;
    color: var(--white);
  }
  .board {
    position: relative;
    width: 1200px;
    height: 1200px;
    display: grid;
    grid-template-columns: 300px 300px;
    grid-template-rows: 534px 534px;
    gap: 44px 100px;
    justify-content: center;
    align-content: center;
  }
  .screen {
    position: relative;
    overflow: hidden;
    box-shadow: 0 20px 50px rgba(0,0,0,.5);
  }
  /* shared header */
  .app-header {
    height: 96px;
    background: var(--header);
    position: relative;
    text-align: center;
  }
  .menu-icon { position: absolute; left: 18px; top: 58px; }
  .brand {
    display: inline-flex; align-items: center; gap: 6px;
    margin-top: 14px; font-weight: 700; font-size: 15px; color: var(--white);
  }
  .brand-dot { width: 9px; height: 9px; border-radius: 50%; background: var(--accent); }
  .screen-title {
    font-size: 15px; letter-spacing: 1px; font-weight: 400;
    margin-top: 12px; color: var(--accent);
  }
  .nav-arrow { position: absolute; top: 60px; }

  /* office location */
  .office { background: var(--light); }
  .office-body {
    height: 438px;
    background: linear-gradient(135deg, #e4e4e4 0%, #fafafa 45%, #dedede 46%, #f6f6f6 100%);
    display: flex; align-items: center; justify-content: center;
  }
  .door-button {
    width: 168px; height: 168px; border-radius: 50%;
    background: radial-gradient(circle, #ffffff 55%, #eeeeee 100%);
    border: 5px solid #0c1b25;
    box-shadow: 0 0 0 4px #8fe0ff, 0 0 0 10px rgba(0,178,255,.25), 0 0 40px 14px rgba(0,178,255,.35);
    display: flex; align-items: center; justify-content: center; gap: 8px;
    color: var(--ink); font-size: 26px; font-weight: 500; letter-spacing: 1px;
  }

  /* welcome */
  .welcome {
    background: var(--panel-dark);
  }
  .welcome-photo {
    position: absolute; inset: 0;
    background: linear-gradient(160deg, #3a2a2e 0%, #4a3a3c 30%, #2a2a2e 60%, #1a1a1a 100%);
  }
  .welcome-shade { position: absolute; inset: 0; background: linear-gradient(180deg, rgba(20,20,20,.2), rgba(20,20,20,.75)); }
  .welcome-content { position: relative; padding: 96px 30px 0; }
  .welcome-brand { font-size: 40px; font-weight: 700; display: flex; align-items: center; gap: 10px; }
  .welcome-brand .brand-dot { width: 16px; height: 16px; }
  .welcome-kicker { margin-top: 26px; font-size: 17px; font-weight: 500; color: var(--accent); letter-spacing: 1px; }
  .welcome-company { font-size: 13px; font-weight: 500; letter-spacing: 1px; margin-top: 4px; }
  .welcome-actions { position: absolute; left: 30px; right: 30px; bottom: 70px; }
  .btn {
    display: block; height: 44px; border-radius: 22px; line-height: 44px;
    text-align: center; font-size: 14px; font-weight: 600;
  }
  .btn-primary { background: var(--accent); color: var(--white); }
  .btn-outline { border: 1px solid rgba(255,255,255,.8); margin-top: 14px; color: var(--white); }
  .help-link { position: absolute; right: 24px; bottom: 26px; font-size: 12px; color: var(--muted); }

  /* profile */
  .profile { background: var(--panel-dark); }
  .profile .app-header { height: 74px; text-align: left; }
  .profile .screen-title { color: var(--white); margin: 0; position: absolute; top: 30px; left: 0; right: 0; text-align: center; font-size: 13px; }
  .profile .menu-icon { top: 30px; }
  .power-icon { position: absolute; right: 18px; top: 26px; }
  .avatar {
    width: 80px; height: 80px; border-radius: 50%; margin: 18px auto 22px;
    background: radial-gradient(circle at 50% 40%, #6a5a52, #2c2f36);
  }
  .field {
    height: 40px; margin: 0 22px 12px; border-radius: 20px; background: var(--field);
    display: flex; align-items: center; gap: 12px; padding: 0 16px; font-size: 12px;
  }
  .dots { letter-spacing: 3px; font-size: 16px; font-weight: 700; }
  .notification {
    position: absolute; left: 0; right: 0; bottom: 0; height: 146px;
    background: var(--white); color: var(--ink); padding: 26px 30px;
  }
  .notification h3 { color: var(--accent); font-size: 13px; font-weight: 600; letter-spacing: 1px; }
  .notification p { font-size: 12px; margin-top: 14px; }

  /* 3d touch */
  .touch { background: var(--panel-black); }
  .touch-visual {
    height: 280px; background: linear-gradient(160deg, var(--accent) 0%, #22bfff 60%, #e8f6fc 100%);
  }
  .touch-copy { padding: 30px 30px 0; text-align: center; }
  .touch-copy h2 { font-size: 22px; font-weight: 600; }
  .touch-copy p { margin-top: 12px; font-size: 11px; line-height: 1.6; color: #bfbfbf; }
  .touch .btn-outline { margin: 24px 40px 0; font-size: 13px; letter-spacing: 3px; font-weight: 700; }
  .skip { text-align: center; margin-top: 16px; font-size: 13px; }
</style>
</head>
<body>
<main class="board">

  <section class="screen office">
    <header class="app-header">
      <svg class="menu-icon" width="20" height="14" viewBox="0 0 20 14"><path d="M0 1h20M4 7h16M0 13h20" stroke="#fff" stroke-width="1.5"/></svg>
      <div class="brand"><span class="brand-dot"></span>Wopel</div>
      <h1 class="screen-title">OFFICE LOCATION</h1>
      <svg class="nav-arrow" style="left:16px" width="8" height="14" viewBox="0 0 8 14"><path d="M7 1L1 7l6 6" fill="none" stroke="#00b2ff" stroke-width="1.5"/></svg>
      <svg class="nav-arrow" style="right:16px" width="8" height="14" viewBox="0 0 8 14"><path d="M1 1l6 6-6 6" fill="none" stroke="#00b2ff" stroke-width="1.5"/></svg>
    </header>
    <div class="office-body">
      <div class="door-button">
        <svg width="22" height="20" viewBox="0 0 22 20"><path d="M11 0L0 10l11 10z" fill="#00b2ff"/><path d="M22 0L11 10l11 10z" fill="#7fd8ff"/></svg>
        DOOR
      </div>
    </div>
  </section>

  <section class="screen welcome">
    <div class="welcome-photo" role="img" aria-label="Photo of a hand holding a smartphone"></div>
    <div class="welcome-shade"></div>
    <div class="welcome-content">
      <div class="welcome-brand"><span class="brand-dot"></span>Wopel</div>
      <p class="welcome-kicker">WELCOME</p>
      <p class="welcome-company">QUILLSTONE ACCESS CONTROLS</p>
    </div>
    <div class="welcome-actions">
      <span class="btn btn-primary">Log in</span>
      <span class="btn btn-outline">Sign up</span>
    </div>
    <span class="help-link">Need Help?</span>
  </section>

  <section class="screen profile">
    <header class="app-header">
      <svg class="menu-icon" width="20" height="14" viewBox="0 0 20 14"><path d="M0 1h20M4 7h16M0 13h20" stroke="#fff" stroke-width="1.5"/></svg>
      <h1 class="screen-title">PROFILE SETTINGS</h1>
      <svg class="power-icon" width="20" height="20" viewBox="0 0 20 20"><path d="M6 4a8 8 0 1 0 8 0" fill="none" stroke="#fff" stroke-width="1.4"/><path d="M10 1v8" stroke="#fff" stroke-width="1.4"/></svg>
    </header>
    <div class="avatar" role="img" aria-label="Profile photo of the user"></div>
    <div class="field">
      <svg width="16" height="10" viewBox="0 0 16 10"><path d="M0 2h16M3 8h13" stroke="#888" stroke-width="1.2"/></svg>
      Mara Lindqvist
    </div>
    <div class="field">
      <svg width="16" height="12" viewBox="0 0 16 12"><rect x=".6" y=".6" width="14.8" height="10.8" fill="none" stroke="#888" stroke-width="1.2"/><path d="M1 1l7 6 7-6" fill="none" stroke="#888" stroke-width="1.2"/></svg>
      mara.lindqvist@quillstone.io
    </div>
    <div class="field">
      <svg width="14" height="16" viewBox="0 0 14 16"><rect x="1" y="7" width="12" height="8" rx="2" fill="none" stroke="#888" stroke-width="1.2"/><path d="M3.5 7V4.5a3.5 3.5 0 0 1 7 0V7" fill="none" stroke="#888" stroke-width="1.2"/></svg>
      <span class="dots">••••••••</span>
    </div>
    <div class="notification">
      <h3>NOTIFICATION</h3>
      <p>Enable Push Notification</p>
      <p>Enable Sound Alert</p>
    </div>
  </section>

  <section class="screen touch">
    <div class="touch-visual" role="img" aria-label="Illustration of a phone showing the login form with Touch ID"></div>
    <div class="touch-copy">
      <h2>3D Touch Support</h2>
      <p>Support the 3D Touch feature<br>allows you to automatic login</p>
    </div>
    <span class="btn btn-outline">READY TO GO</span>
    <p class="skip">Skip</p>
  </section>

</main>
</body>
</html>
```